Uprising SaaS company needs an attractive business card design

We're an uprising SaaS company who's attempting to attack the rigid car (insurance) claims management market in Europe.
We want to our mighty base order management system, listen to our clients to connect the smart ideas to build something even mightier.
We primarily focus on helping our customers manage their customers' claims/orders and get them resolved as smoothly as possible.
We'd like the business card design to express technical innovation and the fact that we connect smart ideas, as our company slogan indicates.
Contact Information for Business Card
Name, position, website, email, mobile, business address
Colors
Designer to choose colors to be used in the design.
Look and feel
Each slider illustrates characteristics of the customer's brand and the style your logo design should communicate.

```html
<!DOCTYPE html>
<html lang="en">
<head>
<meta charset="utf-8">
<title>nexalyn business card</title>
<link href="https://fonts.googleapis.com/css2?family=Montserrat:wght@400;700&display=swap" rel="stylesheet">
<style>
  :root {
    --backdrop: #d6d6d6;
    --card-light: #ffffff;
    --card-dark: #000000;
    --ink-grey: #6f6f6f;
    --ink-soft: #4a4a4a;
    --accent-blue: #7ccbe3;
    --rule-grey: #9a9a9a;
  }
  * { margin: 0; padding: 0; box-sizing: border-box; }
  html, body {
    width: 1200px;
    height: 913px;
    overflow: hidden;
    background: var(--backdrop);
    font-family: "Montserrat", sans-serif;
  }
  .canvas {
    width: 1200px;
    height: 913px;
    display: flex;
    flex-direction: column;
    align-items: center;
    justify-content: center;
    gap: 36px;
  }
  .card {
    width: 700px;
    height: 400px;
    box-shadow: 0 10px 28px rgba(0,0,0,0.25);
    position: relative;
  }
  .card--front {
    background: var(--card-light);
    display: flex;
    align-items: center;
  }
  .card--back {
    background: var(--card-dark);
    display: flex;
    align-items: center;
    justify-content: center;
  }
  .brand-name {
    font-family: "Montserrat", sans-serif;
    font-weight: 400;
    color: var(--accent-blue);
    letter-spacing: 0.02em;
  }
  .front-brand {
    width: 350px;
    text-align: center;
    font-size: 40px;
  }
  .divider {
    width: 1px;
    height: 250px;
    background: var(--rule-grey);
  }
  .contact {
    padding-left: 34px;
    color: var(--ink-soft);
    font-size: 15px;
    line-height: 1.55;
  }
  .contact__name {
    font-weight: 700;
    font-size: 24px;
    color: var(--ink-grey);
    letter-spacing: 0.01em;
    line-height: 1.1;
  }
  .contact__role {
    font-size: 16px;
    margin-bottom: 14px;
  }
  .contact__row {
    display: flex;
    align-items: center;
    gap: 10px;
  }
  .contact__icon {
    width: 14px;
    height: 14px;
    flex: none;
  }
  .contact__address {
    margin-top: 14px;
    font-size: 16px;
    line-height: 1.4;
  }
  .back-brand {
    font-size: 96px;
  }
</style>
</head>
<body>
  <main class="canvas">
    <section class="card card--front">
      <div class="front-brand brand-name">nexalyn</div>
      <div class="divider"></div>
      <div class="contact">
        <div class="contact__name">DANIEL MARSH</div>
        <div class="contact__role">Managing Director</div>
        <div class="contact__row">
          <svg class="contact__icon" viewBox="0 0 14 14" aria-hidden="true">
            <path d="M3 1.5 L5 1.5 L6 4.5 L4.5 5.5 Q5.5 8 8.5 9.5 L9.5 8 L12.5 9 L12.5 11 Q12 12.5 10.5 12.5 Q2 11.5 1.5 3.5 Q1.5 2 3 1.5 Z" fill="var(--accent-blue)"/>
          </svg>
          <span>031-555 208 417</span>
        </div>
        <div class="contact__row">
          <svg class="contact__icon" viewBox="0 0 14 14" aria-hidden="true">
            <rect x="1" y="3" width="12" height="8.5" fill="var(--accent-blue)"/>
            <path d="M1 3 L7 8 L13 3" fill="none" stroke="#fff" stroke-width="1"/>
          </svg>
          <span>hello@nexalyn.io</span>
        </div>
        <div class="contact__row">
          <svg class="contact__icon" viewBox="0 0 14 14" aria-hidden="true">
            <circle cx="7" cy="7" r="6" fill="var(--accent-blue)"/>
            <path d="M1 7 H13 M7 1 Q3.5 7 7 13 M7 1 Q10.5 7 7 13" fill="none" stroke="#fff" stroke-width="0.8"/>
          </svg>
          <span>www.nexalyn.io</span>
        </div>
        <div class="contact__address">
          18, Harbour Lane<br>
          Rotterdam, 30112
        </div>
      </div>
    </section>
    <section class="card card--back">
      <div class="back-brand brand-name">nexalyn</div>
    </section>
  </main>
</body>
</html>
```